Santa Crying/Smiling Graphic for stickers and t-shirts

This graphic will be printed on t-shirts and stickers. It needs to be round in general shape. We will be giving stickers to kids after they take a photo with Santa Claus, Some kids cry, some smile.

The project needs to contain two graphic files, one of the smiling sticker, and one of the crying sticker. We are okay with a cartoon drawing if you want, or a text only design, but they need to go together but easily contrast each other. The text will say "I smiled for Santa" or "I cried for Santa". The design must have our logo as part of it somehow, and include the year "2016", as we want to renew this every year.

I included the logo we would like you to use. The smile graphic will be printed on mint blue, and the crying graphic will be printed on red. Please use colors that match that scheme. Thank you!
Updates

Target Market(s)

Families and children

Font styles to use
Sans Serif

Colors
ec1f27
cee9f5
0355a3
9bcb3c

Requirements
Must have
• "I smiled for Santa" in one design, printed on mint blue
• "I cried for Santa" in second design, printed on Christmas red
• "2016" on both
• Our logo on both
Nice to have
• Similar style for tboth
Should not have
• NA

```html
<!DOCTYPE html>
<html lang="en">
<head>
<meta charset="utf-8">
<title>Santa Sticker Pair</title>
<link rel="stylesheet" href="https://fonts.googleapis.com/css2?family=Signika:wght@400;500&display=swap">
<style>
  :root {
    --page: #ffffff;
    --mint: #cee9f5;
    --navy: #0b55a3;
    --red: #ec1f27;
    --green: #9bcb3c;
    --white: #ffffff;
    --blush: #f0908f;
    --grey: #a9a9ad;
    --art-mint: #e2f2f9;
    --art-navy: #2265ad;
  }
  html, body {
    margin: 0;
    width: 1200px;
    height: 1000px;
    overflow: hidden;
    background: var(--page);
  }
  .canvas { display: block; width: 1200px; height: 1000px; }
  .sticker-text {
    font-family: "Signika", sans-serif;
    font-weight: 500;
    paint-order: stroke;
    stroke: var(--white);
    stroke-linejoin: round;
  }
  .headline-arc { font-size: 64px; stroke-width: 6px; }
  .headline-santa { font-size: 112px; stroke-width: 7px; }
  .smiled .sticker-text { fill: var(--red); }
  .cried .sticker-text { fill: var(--green); }
  .smiled .disc { fill: var(--mint); }
  .cried .disc { fill: var(--navy); }
  .smiled .santa-art { fill: var(--art-mint); }
  .cried .santa-art { fill: var(--art-navy); }
  .studio-name {
    font-family: "Signika", sans-serif;
    font-weight: 400;
    fill: var(--blush);
    letter-spacing: 2px;
  }
  .studio-name .line-main { font-size: 25px; }
  .studio-name .line-sub { font-size: 15px; letter-spacing: 2.5px; }
  .year {
    font-family: "Signika", sans-serif;
    font-weight: 400;
    font-size: 22px;
    fill: var(--grey);
    letter-spacing: 1px;
  }
</style>
</head>
<body>
<svg class="canvas" viewBox="0 0 1200 1000" xmlns="http://www.w3.org/2000/svg">
  <defs>
    <path id="arc-left" d="M 87 546 A 246 246 0 0 1 579 546"/>
    <path id="arc-right" d="M 630 546 A 246 246 0 0 1 1122 546"/>
  </defs>

  <g class="sticker smiled">
    <circle class="disc" cx="329" cy="494" r="250"/>
    <ellipse class="santa-art" cx="345" cy="400" rx="105" ry="120" role="img" aria-label="Line drawing of Santa Claus giving a thumbs up"/>
    <text class="sticker-text headline-arc" text-anchor="middle">
      <textPath href="#arc-left" startOffset="50%">I smiled for</textPath>
    </text>
    <text class="sticker-text headline-santa" x="333" y="518" text-anchor="middle">Santa</text>
    <text class="studio-name" text-anchor="middle">
      <tspan class="line-main" x="329" y="667">THE HOLLOWAYS’</tspan>
      <tspan class="line-sub" x="329" y="688">PHOTOGRAPHY</tspan>
    </text>
    <text class="year" x="325" y="713" text-anchor="middle">2016</text>
  </g>

  <g class="sticker cried">
    <circle class="disc" cx="872" cy="494" r="250"/>
    <ellipse class="santa-art" cx="888" cy="400" rx="105" ry="120" role="img" aria-label="Line drawing of Santa Claus giving a thumbs up"/>
    <text class="sticker-text headline-arc" text-anchor="middle">
      <textPath href="#arc-right" startOffset="50%">I cried for</textPath>
    </text>
    <text class="sticker-text headline-santa" x="876" y="518" text-anchor="middle">Santa</text>
    <text class="studio-name" text-anchor="middle">
      <tspan class="line-main" x="872" y="667">THE HOLLOWAYS’</tspan>
      <tspan class="line-sub" x="872" y="688">PHOTOGRAPHY</tspan>
    </text>
    <text class="year" x="868" y="713" text-anchor="middle">2016</text>
  </g>
</svg>
</body>
</html>
```